Calloway needs a modernized design

We would like a modern update (that can be responsive) to our existing website. Attached are the two existing pages we would like new concepts of - our home page and a page about one of our locations.

Calloway is provides executive offices and virtual office services. Startups, law firms, and financial services are our primary clients. We would like a professional, clean design, leaning towards minimalist. We intend to greatly reduce/eliminate the long paragraphs of text.

Industry/Entity Type

Business Service

Number of Pages Required

2 page

Requirements
Must have
• A design that can be responsive
Nice to have
• Large image(s) on home page that rotate.

```html
<!DOCTYPE html>
<html lang="en">
<head>
<meta charset="utf-8">
<title>Calloway Business Centers</title>
<link rel="stylesheet" href="https://fonts.googleapis.com/css2?family=Cinzel:wght@400;700&family=Lato:wght@400;700;900&display=swap">
<style>
:root{
  --navy:#26335f;
  --navy-deep:#1e2a52;
  --orange:#f39322;
  --orange-light:#f7a640;
  --text:#3b3b3b;
  --muted:#666;
  --gray-bg:#ececec;
  --line:#c9ccd6;
  --white:#fff;
  --red:#d8412f;
  --blue:#2f9fd8;
  --indigo:#1d6fb0;
  --crimson:#c8232c;
}
*{box-sizing:border-box;margin:0;padding:0}
html,body{width:1200px;height:2769px;overflow:hidden}
body{position:relative;background:var(--white);font-family:"Lato",Arial,sans-serif;color:var(--text)}
.abs{position:absolute}
.serif{font-family:"Cinzel",Georgia,serif}

/* header */
.top-rule{left:0;top:0;width:1200px;height:3px;background:var(--navy)}
.brand{left:61px;top:26px;display:flex;align-items:center;gap:14px}
.brand-dot{width:70px;height:70px;border-radius:50%;background:var(--navy)}
.brand-name{font-family:"Cinzel",Georgia,serif;font-weight:700;font-size:30px;line-height:1;color:var(--navy)}
.brand-name small{display:block;font-size:15px;margin-top:6px;letter-spacing:1px}
.social-top{left:824px;top:10px;display:flex;gap:7px}
.social-top span{width:22px;height:22px;border-radius:50%}
.phone-tab{left:968px;top:0;width:200px;height:34px;background:var(--navy);border-radius:0 0 0 24px;color:#fff;font-size:17px;display:flex;align-items:center;justify-content:center;gap:10px}
.nav{left:470px;top:66px;display:flex;align-items:center;font-family:"Cinzel",Georgia,serif;font-size:16px;color:#222;letter-spacing:.5px}
.nav a{color:inherit;text-decoration:none;padding:0 14px;border-left:1px solid #bbb;line-height:14px}
.nav a.home{border:none;padding:0 14px 0 0}

/* hero */
.hero{left:0;top:111px;width:1200px;height:507px;background:linear-gradient(180deg,#5b3a2a 0%,#3e2d2a 40%,#2b2b38 70%,#3a3f9a 100%)}
.hero-badge{left:812px;top:203px;width:314px;height:314px;border-radius:50%;background:rgba(40,40,44,.78);border:6px solid rgba(255,255,255,.35);display:flex;flex-direction:column;align-items:center;justify-content:center;color:#fff;text-align:center}
.hero-badge .mark{width:64px;height:64px;border-radius:50%;background:rgba(255,255,255,.25);margin-bottom:22px}
.hero-badge p{font-family:"Lato",Arial,sans-serif;font-weight:700;font-size:26px;line-height:31px}
.dots{display:flex;gap:6px;margin-top:16px}
.dots i{width:8px;height:8px;border-radius:50%;background:#999}
.dots i.on{background:var(--orange)}
.hero-arrow{top:355px;width:24px;height:46px;background:rgba(255,255,255,.85);display:flex;align-items:center;justify-content:center}

/* welcome */
.h-section{font-family:"Cinzel",Georgia,serif;color:var(--navy);font-size:37px;letter-spacing:1px;text-align:center;width:1200px;left:0}
.divider{left:290px;width:620px;height:24px}
.welcome-lead{left:80px;top:754px;width:1040px;text-align:center;font-weight:700;color:var(--navy);font-size:19px;line-height:27px}
.welcome-text{left:60px;top:822px;width:1080px;text-align:center;font-size:15px;line-height:25px;color:#444}
.btn{display:flex;align-items:center;gap:8px;height:30px;border-radius:15px;padding:0 14px 0 4px;font-size:14px;font-weight:700;color:#fff}
.btn .pip{width:24px;height:24px;border-radius:50%;background:var(--navy)}
.btn-orange{background:var(--orange)}
.btn-navy{background:var(--navy)}
.btn-navy .pip{background:#fff}

/* split */
.split-left{left:0;top:1008px;width:595px;height:465px;background:linear-gradient(135deg,#2c3a6b,#253160)}
.split-right{left:595px;top:1008px;width:605px;height:465px;background:linear-gradient(135deg,#f59a2a,#e9891a)}
.notch{left:570px;top:1008px;width:50px;height:20px}
.link-line{left:390px;top:1129px;width:430px;height:2px;background:rgba(255,255,255,.5)}
.icon-disc{width:130px;height:130px;border-radius:50%;display:flex;align-items:center;justify-content:center}
.center-disc{left:557px;top:1093px;width:76px;height:76px;border-radius:50%;background:#fff;border:5px solid var(--navy)}
.split-title{font-family:"Cinzel",Georgia,serif;font-size:31px;letter-spacing:1px;text-align:center}
.ticks{list-style:none;font-size:14px;font-weight:700;color:#fff}
.ticks li{display:flex;align-items:center;gap:8px;height:30px}
.tick{width:14px;height:14px;border-radius:50%;display:inline-flex;align-items:center;justify-content:center}

/* community / services */
.community{left:0;top:1473px;width:595px;height:552px;background:linear-gradient(90deg,#fff 0%,#f1f1f1 70%,#e2e2e2 100%)}
.services{left:595px;top:1473px;width:605px;height:552px;background:var(--gray-bg)}
.h-block{font-family:"Cinzel",Georgia,serif;color:var(--navy);font-size:36px;letter-spacing:1px}
.h-rule{height:1px;background:#d0d0d0}
.community-photo{left:61px;top:1602px;width:489px;height:201px;background:linear-gradient(120deg,#7a5a44,#b48a66 45%,#8a6b55)}
.community-text{left:61px;top:1822px;width:489px;font-size:13px;line-height:20px;color:#333}
.more{font-size:14px;font-weight:700;color:var(--navy)}
.service{left:641px;width:500px}
.service-icon{position:absolute;left:0;top:0;width:62px;height:62px;border-radius:50%;background:#2c2c2c;display:flex;align-items:center;justify-content:center}
.service h3{margin-left:75px;font-size:20px;color:var(--orange);font-weight:700}
.service p{margin-left:75px;font-size:13px;line-height:19px;color:#333;margin-top:6px}
.service .more{display:block;margin-left:75px;margin-top:8px}
.dotted{left:641px;width:500px;border-top:1px dashed #aaa}

/* partners */
.partner{top:2195px;width:157px;height:74px;border:1px solid #cfcfcf;background:#fff;display:flex;align-items:center;justify-content:center}
.partner span{width:96px;height:28px;border-radius:4px;background:#d8d8d8}
.partner-arrow{top:2210px;width:20px;height:44px}

/* footer */
.footer{left:0;top:2330px;width:1200px;height:393px}
.footer-disc{left:559px;top:2313px;width:82px;height:82px;border-radius:50%;background:#fff;border:6px solid var(--navy)}
.footer-disc i{display:block;width:44px;height:44px;border-radius:50%;background:var(--navy);margin:13px auto}
.f-col{color:#fff}
.f-col h4{font-family:"Cinzel",Georgia,serif;font-weight:400;font-size:21px;letter-spacing:1px;padding-bottom:14px;border-bottom:1px solid rgba(255,255,255,.25);margin-bottom:18px}
.f-links{list-style:none;font-size:13px;line-height:34px}
.f-links li::before{content:"";display:inline-block;width:5px;height:5px;border-radius:50%;background:var(--orange);margin-right:12px;vertical-align:middle}
.contact-row{display:flex;gap:12px;font-size:13px;line-height:20px;margin-bottom:14px}
.contact-row svg{flex:none;margin-top:2px}
.field{width:277px;height:37px;background:#fff;border-radius:2px;margin-bottom:8px;font-size:13px;color:#888;padding:10px 12px}
.field.tall{height:37px}
.submit{width:129px;height:35px;background:#3d5199;color:#fff;font-weight:700;font-size:15px;display:flex;align-items:center;justify-content:center;margin-top:8px}
.follow{list-style:none;font-size:13px;font-weight:700}
.follow li{display:flex;align-items:center;gap:12px;height:46px}
.follow span{width:32px;height:32px;border-radius:50%}
.copyright{left:0;top:2723px;width:1200px;height:46px;background:var(--orange);color:#fff;font-size:13px;font-weight:700;display:flex;align-items:center;justify-content:center}
</style>
</head>
<body>

<!-- header -->
<div class="abs top-rule"></div>
<div class="abs brand">
  <span class="brand-dot"></span>
  <div class="brand-name">Calloway<small>Business Centers</small></div>
</div>
<div class="abs social-top">
  <span style="background:var(--red)"></span>
  <span style="background:var(--indigo)"></span>
  <span style="background:var(--blue)"></span>
  <span style="background:#dd4b39"></span>
</div>
<div class="abs phone-tab">
  <svg width="18" height="18" viewBox="0 0 24 24"><path d="M6.6 10.8a15 15 0 0 0 6.6 6.6l2.2-2.2a1 1 0 0 1 1-.25 11.4 11.4 0 0 0 3.6.57 1 1 0 0 1 1 1V20a1 1 0 0 1-1 1A17 17 0 0 1 3 4a1 1 0 0 1 1-1h3.5a1 1 0 0 1 1 1c0 1.25.2 2.45.57 3.6a1 1 0 0 1-.25 1z" fill="#fff"/></svg>
  <span>+ 214.555.0187</span>
</div>
<nav class="abs nav">
  <a class="home" href="#"><svg width="26" height="24" viewBox="0 0 26 24"><path d="M13 2 1 12h4v10h6v-6h4v6h6V12h4z" fill="var(--navy)"/></svg></a>
  <a href="#">Properties</a>
  <a href="#">Virtual Tours &amp; Videos</a>
  <a href="#">Photos</a>
  <a href="#">Broker Referrals</a>
</nav>

<!-- hero -->
<div class="abs hero" role="img" aria-label="Photo of a boardroom with a long wooden table, black leather chairs and a bright patterned carpet"></div>
<div class="abs hero-badge">
  <span class="mark"></span>
  <p>We Provide Executive<br>Offices &nbsp;And Virtual<br>Office Services</p>
  <div class="dots"><i class="on"></i><i></i><i></i></div>
</div>
<div class="abs hero-arrow" style="left:0;border-radius:0 23px 23px 0"><svg width="10" height="14" viewBox="0 0 10 14"><path d="M8 1 2 7l6 6" stroke="#333" stroke-width="2" fill="none"/></svg></div>
<div class="abs hero-arrow" style="left:1176px;border-radius:23px 0 0 23px"><svg width="10" height="14" viewBox="0 0 10 14"><path d="m2 1 6 6-6 6" stroke="#333" stroke-width="2" fill="none"/></svg></div>

<!-- welcome -->
<h1 class="abs h-section" style="top:655px;font-weight:400">Welcome to Calloway Business Centers</h1>
<svg class="abs divider" style="top:708px" viewBox="0 0 620 24"><line x1="0" y1="12" x2="288" y2="12" stroke="var(--line)"/><line x1="332" y1="12" x2="620" y2="12" stroke="var(--line)"/><circle cx="310" cy="12" r="11" fill="var(--navy)"/></svg>
<p class="abs welcome-lead">Come See Why Smarter Companies are Choosing Calloway Business Centers' Dallas, Ft. Worth and Houston Executive Office Suites, Virtual Offices, Meeting Rooms and Video Conferencing.</p>
<p class="abs welcome-text">Either you need Dallas/Ft. Worth Office Space, Dallas Executive Suites, Ft. Worth Executive Suites, Houston Office Space, Houston Executive Suites,<br>or maybe you simply need a place to stop in and use an on-demand office or meeting room from time to time or utilize our local business phone numbers, phone<br>answering or business addresses through one of our virtual office solutions</p>
<div class="abs btn btn-orange" style="left:532px;top:921px"><span class="pip"></span>Read More &raquo;</div>

<!-- executive / virtual -->
<div class="abs split-left" role="img" aria-label="Navy tinted photo of colleagues at work"></div>
<div class="abs split-right" role="img" aria-label="Orange tinted photo of a team meeting"></div>
<svg class="abs notch" viewBox="0 0 50 20"><path d="M0 0h50L25 20z" fill="#fff"/></svg>
<div class="abs link-line"></div>
<div class="abs icon-disc" style="left:243px;top:1065px;background:var(--orange);border:4px solid rgba(255,255,255,.6)">
  <svg width="56" height="62" viewBox="0 0 56 62" fill="none" stroke="#fff" stroke-width="4" stroke-linecap="round"><rect x="14" y="4" width="28" height="24" rx="6"/><path d="M8 34h40M28 34v12M14 56l14-10 14 10M6 24v10M50 24v10"/></svg>
</div>
<div class="abs icon-disc" style="left:841px;top:1065px;background:var(--navy);border:4px solid rgba(255,255,255,.6)">
  <svg width="62" height="62" viewBox="0 0 62 62" fill="#fff"><circle cx="20" cy="10" r="7"/><path d="M10 20h18l4 18H24l-2 20h-6l-2-20H10z"/><rect x="34" y="14" width="22" height="18" rx="2"/><rect x="30" y="36" width="30" height="4"/><rect x="52" y="40" width="4" height="18"/></svg>
</div>
<div class="abs center-disc"></div>

<h2 class="abs split-title" style="left:0;width:595px;top:1208px;color:var(--orange)">Executive Offices</h2>
<ul class="abs ticks" style="left:112px;top:1268px">
  <li><span class="tick" style="background:var(--orange)"><svg width="8" height="8" viewBox="0 0 8 8"><path d="m1 4 2 2 4-4" stroke="#fff" stroke-width="1.6" fill="none"/></svg></span>Full Service Offices</li>
  <li><span class="tick" style="background:var(--orange)"><svg width="8" height="8" viewBox="0 0 8 8"><path d="m1 4 2 2 4-4" stroke="#fff" stroke-width="1.6" fill="none"/></svg></span>Disaster Recovery</li>
  <li><span class="tick" style="background:var(--orange)"><svg width="8" height="8" viewBox="0 0 8 8"><path d="m1 4 2 2 4-4" stroke="#fff" stroke-width="1.6" fill="none"/></svg></span>All-Inclusive Pricing!</li>
</ul>
<ul class="abs ticks" style="left:293px;top:1268px">
  <li><span class="tick" style="background:var(--orange)"><svg width="8" height="8" viewBox="0 0 8 8"><path d="m1 4 2 2 4-4" stroke="#fff" stroke-width="1.6" fill="none"/></svg></span>Flexible Contracts from $395</li>
  <li><span class="tick" style="background:var(--orange)"><svg width="8" height="8" viewBox="0 0 8 8"><path d="m1 4 2 2 4-4" stroke="#fff" stroke-width="1.6" fill="none"/></svg></span>Corporate or Satellite Offices</li>
</ul>
<div class="abs btn btn-orange" style="left:236px;top:1386px"><span class="pip"></span>Read More &raquo;</div>

<h2 class="abs split-title" style="left:595px;width:605px;top:1208px;color:#fff">Virtual Office</h2>
<ul class="abs ticks" style="left:705px;top:1268px">
  <li><span class="tick" style="background:var(--navy)"><svg width="8" height="8" viewBox="0 0 8 8"><path d="m1 4 2 2 4-4" stroke="#fff" stroke-width="1.6" fill="none"/></svg></span>Mailing Address $49/mo</li>
  <li><span class="tick" style="background:var(--navy)"><svg width="8" height="8" viewBox="0 0 8 8"><path d="m1 4 2 2 4-4" stroke="#fff" stroke-width="1.6" fill="none"/></svg></span>Local Phone &amp; Mail $99/mo</li>
  <li><span class="tick" style="background:var(--navy)"><svg width="8" height="8" viewBox="0 0 8 8"><path d="m1 4 2 2 4-4" stroke="#fff" stroke-width="1.6" fill="none"/></svg></span>Corporate or Satellite Offices</li>
</ul>
<ul class="abs ticks" style="left:949px;top:1268px">
  <li><span class="tick" style="background:var(--navy)"><svg width="8" height="8" viewBox="0 0 8 8"><path d="m1 4 2 2 4-4" stroke="#fff" stroke-width="1.6" fill="none"/></svg></span>Flexible Contracts</li>
  <li><span class="tick" style="background:var(--navy)"><svg width="8" height="8" viewBox="0 0 8 8"><path d="m1 4 2 2 4-4" stroke="#fff" stroke-width="1.6" fill="none"/></svg></span>All-Inclusive Pricing!</li>
</ul>
<div class="abs btn btn-navy" style="left:834px;top:1386px"><span class="pip"></span>Read More &raquo;</div>

<!-- community -->
<div class="abs community"></div>
<h2 class="abs h-block" style="left:61px;top:1516px;font-weight:400">Community</h2>
<div class="abs h-rule" style="left:61px;top:1572px;width:489px"></div>
<div class="abs community-photo" role="img" aria-label="Photo of many hands stacked together over a wooden table"></div>
<p class="abs community-text">Lorem ipsum dolor sit amet, consectetuer adipiscing elit, sed diam nonummy nibh euismod tincidunt ut laoreet dolore magna aliquam erat volutpat. Ut wisi enim ad minim veniam, quis nostrud exerci tation ullamcorper suscipit lobortis nisl utiquip ex ea commodo consequat. Duis autem vel eum iriure dolor in hendrerit inputate velit esse molestie consequat, vel illum dolore eu feugiat nulla facilisis at vero eros et accumsan et iusto odio dignissim qui blandit</p>
<span class="abs more" style="left:63px;top:1955px">Read More &raquo;</span>

<!-- other services -->
<div class="abs services"></div>
<h2 class="abs h-block" style="left:641px;top:1516px;font-weight:400;font-size:33px">Other Services</h2>
<div class="abs h-rule" style="left:641px;top:1572px;width:500px"></div>

<div class="abs service" style="top:1602px">
  <div class="service-icon"><svg width="36" height="30" viewBox="0 0 36 30" fill="#fff"><rect x="8" y="12" width="20" height="6" rx="2"/><circle cx="12" cy="6" r="3"/><circle cx="24" cy="6" r="3"/><circle cx="12" cy="25" r="3"/><circle cx="24" cy="25" r="3"/><circle cx="3" cy="15" r="3"/><circle cx="33" cy="15" r="3"/></svg></div>
  <h3>On-demand Meeting Rooms</h3>
  <p>Lorem ipsum dolor sit amet, consectetuer adipiscing elit, sed diam my nibh euismod dloer sknev cjsrewvc bnarv bdivrt.</p>
  <span class="more">Read More &raquo;</span>
</div>
<div class="abs dotted" style="top:1719px"></div>
<div class="abs service" style="top:1739px">
  <div class="service-icon"><svg width="36" height="36" viewBox="0 0 36 36" fill="#fff"><circle cx="18" cy="18" r="7"/><circle cx="18" cy="4" r="3"/><circle cx="18" cy="32" r="3"/><circle cx="4" cy="18" r="3"/><circle cx="32" cy="18" r="3"/><circle cx="8" cy="8" r="3"/><circle cx="28" cy="28" r="3"/><circle cx="28" cy="8" r="3"/><circle cx="8" cy="28" r="3"/></svg></div>
  <h3>On-demand Training Rooms</h3>
  <p>Lorem ipsum dolor sit amet, consectetuer adipiscing elit, sed diam my nibh euismod dloer sknev cjsrewvc bnarv bdivrt.</p>
  <span class="more">Read More &raquo;</span>
</div>
<div class="abs dotted" style="top:1855px"></div>
<div class="abs service" style="top:1875px">
  <div class="service-icon"><svg width="36" height="32" viewBox="0 0 36 32" fill="#fff"><circle cx="18" cy="7" r="5"/><path d="M10 22a8 8 0 0 1 16 0z"/><circle cx="6" cy="14" r="3.5"/><circle cx="30" cy="14" r="3.5"/><path d="M0 28a6 6 0 0 1 12 0zM24 28a6 6 0 0 1 12 0z"/></svg></div>
  <h3>Virtual Office Solutions</h3>
  <p>Lorem ipsum dolor sit amet, consectetuer adipiscing elit, sed diam my nibh euismod dloer sknev cjsrewvc bnarv bdivrt.</p>
  <span class="more">Read More &raquo;</span>
</div>

<!-- partners -->
<h2 class="abs h-section" style="top:2073px;font-weight:400">Our Partners</h2>
<svg class="abs divider" style="top:2126px" viewBox="0 0 620 24"><line x1="0" y1="12" x2="288" y2="12" stroke="var(--line)"/><line x1="332" y1="12" x2="620" y2="12" stroke="var(--line)"/><circle cx="310" cy="12" r="11" fill="var(--navy)"/></svg>
<svg class="abs partner-arrow" style="left:16px" viewBox="0 0 20 44"><path d="M17 2 3 22l14 20" stroke="#bbb" stroke-width="2" fill="none"/></svg>
<div class="abs partner" style="left:61px"><span></span></div>
<div class="abs partner" style="left:246px"><span></span></div>
<div class="abs partner" style="left:430px"><span></span></div>
<div class="abs partner" style="left:615px"><span></span></div>
<div class="abs partner" style="left:799px"><span></span></div>
<div class="abs partner" style="left:984px"><span></span></div>
<svg class="abs partner-arrow" style="left:1164px" viewBox="0 0 20 44"><path d="m3 2 14 20L3 42" stroke="#bbb" stroke-width="2" fill="none"/></svg>

<!-- footer -->
<svg class="abs footer" viewBox="0 0 1200 393" preserveAspectRatio="none">
  <path d="M0 62Q600-30 1200 62" stroke="#d5d5d5" stroke-width="6" fill="none"/>
  <path d="M0 70Q600-22 1200 70V393H0z" fill="var(--navy)"/>
</svg>
<div class="abs footer-disc"><i></i></div>

<div class="abs f-col" style="left:61px;top:2464px;width:200px">
  <h4>Quick Links</h4>
  <ul class="f-links">
    <li>Home</li><li>Properties</li><li>Virtual Tours &amp; Videos</li><li>Photos</li><li>Broker Referrals</li>
  </ul>
</div>

<div class="abs f-col" style="left:310px;top:2464px;width:240px">
  <h4>Contact Details</h4>
  <div class="contact-row">
    <svg width="12" height="16" viewBox="0 0 12 16"><path d="M6 0a6 6 0 0 1 6 6c0 4.5-6 10-6 10S0 10.5 0 6a6 6 0 0 1 6-6z" fill="var(--orange)"/><circle cx="6" cy="6" r="2.2" fill="var(--navy)"/></svg>
    <div><b>CALLOWAY BUSINESS CENTERS</b><br>4120 Harlow Parkway<br>Suite 300 , Dallas, Texas 75219</div>
  </div>
  <div class="contact-row">
    <svg width="14" height="14" viewBox="0 0 24 24"><path d="M6.6 10.8a15 15 0 0 0 6.6 6.6l2.2-2.2a1 1 0 0 1 1-.25 11.4 11.4 0 0 0 3.6.57 1 1 0 0 1 1 1V20a1 1 0 0 1-1 1A17 17 0 0 1 3 4a1 1 0 0 1 1-1h3.5a1 1 0 0 1 1 1c0 1.25.2 2.45.57 3.6a1 1 0 0 1-.25 1z" fill="var(--orange)"/></svg>
    <div>+ 214.555.0187</div>
  </div>
  <div class="contact-row">
    <svg width="14" height="14" viewBox="0 0 14 14" fill="var(--orange)"><rect x="3" y="0" width="8" height="4"/><rect x="0" y="4" width="14" height="6" rx="1"/><rect x="3" y="9" width="8" height="5"/></svg>
    <div>+ 214.555.0188</div>
  </div>
  <div class="contact-row">
    <svg width="14" height="12" viewBox="0 0 14 12"><rect width="14" height="12" rx="1" fill="var(--orange)"/><path d="m1 1 6 5 6-5" stroke="var(--navy)" fill="none"/></svg>
    <div>Offices@CallowayOffices.com</div>
  </div>
</div>

<div class="abs f-col" style="left:644px;top:2464px;width:280px">
  <h4>Quick Contact</h4>
  <div class="field">Name</div>
  <div class="field">Email</div>
  <div class="field tall">Message</div>
  <div class="submit">Submit</div>
</div>

<div class="abs f-col" style="left:1017px;top:2464px;width:130px">
  <h4>Follow Us</h4>
  <ul class="follow">
    <li><span style="background:#dd4b39"></span>CIRCLECAST</li>
    <li><span style="background:var(--blue)"></span>CHIRPER</li>
    <li><span style="background:var(--indigo)"></span>LINKFOLIO</li>
    <li><span style="background:var(--crimson)"></span>PINBOARDLY</li>
  </ul>
</div>

<div class="abs copyright">Copyright &copy; 2016 &nbsp;Calloway Business Centers. All Rights Reserved.</div>

</body>
</html>
```